Renewable energy website needs a wordpress website

We are a Renewable Energy company specialising in Energy Management, LED Lights and Solar PV Systems based in Kuala Lumpur.
We need wordpress website designed to match our company identity.
We would like to stick with similar shades of blue & green as our logo and to keep it fresh and creative at the same time.

It Company

```html
<!DOCTYPE html>
<html lang="en">
<head>
<meta charset="utf-8">
<title>Verdanta Energy</title>
<link rel="stylesheet" href="https://fonts.googleapis.com/css2?family=Open+Sans:wdth,wght@75..100,400..700&display=swap">
<style>
:root{
  --bar:#1f1f1f;
  --bar-active:#2c2c2c;
  --cyan:#1fb3e0;
  --green:#4c8a26;
  --lime:#8cc63f;
  --body:#fafcfa;
  --text:#5b5b5b;
  --link:#1d4f9c;
  --muted:#777;
  --partner:#c7c7c7;
}
*{margin:0;padding:0;box-sizing:border-box}
html,body{width:965px;height:1200px;overflow:hidden}
body{position:relative;background:var(--body);font-family:"Open Sans",Arial,sans-serif;color:var(--text)}
.abs{position:absolute}
.header{left:0;top:0;width:965px;height:72px;background:var(--bar);border-top:2px solid var(--cyan);box-shadow:0 3px 6px rgba(0,0,0,.4);z-index:2}
.brand{display:flex;align-items:center;gap:7px;font-weight:700;letter-spacing:.5px}
.brand-dot{border-radius:50%;flex:none}
.header .brand{left:156px;top:20px;color:var(--cyan);font-size:13px}
.header .brand-dot{background:var(--cyan);width:26px;height:26px}
.nav{left:409px;top:0;display:flex;height:70px}
.nav a{display:block;padding:0 23px;line-height:66px;font-size:11.5px;font-weight:700;color:#b9b9b9;text-decoration:none}
.nav a.active{background:var(--bar-active);color:#fff;padding:0 18px}
.hero{left:0;top:72px;width:965px;height:361px;background:linear-gradient(100deg,#7a6a52 0%,#a57a5e 20%,#8a8a8a 45%,#b9b9b9 70%,#8e9399 100%)}
.hero-arrow{width:47px;height:47px;background:rgba(30,30,30,.75)}
.caption{left:490px;top:170px;width:343px;height:163px;background:rgba(35,35,35,.78);padding:26px 30px}
.caption h2{font-weight:400;font-size:18px;line-height:26px;color:var(--lime);margin-bottom:8px}
.caption p{font-size:13.5px;line-height:19px;color:#fff;letter-spacing:-.2px}
.hero-edge{left:0;top:433px;width:965px;height:4px;background:#d4d6d6}
.heading{font-stretch:75%;font-weight:700;color:var(--green);white-space:nowrap}
.photo{display:block}
.read{font-size:10px;color:var(--link);text-decoration:underline}
.welcome-title{left:128px;top:463px;font-size:19px}
.welcome-img{left:128px;top:501px;width:165px;height:153px;background:linear-gradient(160deg,#cfd3d6,#5d6168 60%,#2f3238)}
.welcome-text{left:309px;top:502px;width:285px;font-size:9.8px;line-height:13.6px}
.welcome-text p{margin-bottom:13px}
.news-title{left:608px;top:462px;font-size:19px}
.news-item{left:610px;width:230px;height:72px;display:flex;gap:10px}
.news-img{width:69px;height:69px;flex:none}
.news-item h4{font-stretch:75%;font-weight:700;font-size:11.5px;color:var(--green);white-space:nowrap;margin:-2px 0 5px}
.news-item p{font-size:7.4px;line-height:10.5px;color:#555;margin-bottom:5px}
.news-item a{display:block;font-size:7.6px;font-style:italic;color:var(--link);text-decoration:none}
.service{top:690px;width:226px}
.service h3{text-align:center;font-size:19px;height:32px}
.rule{height:5px;border-top:1px dotted #bbb;border-bottom:1px dotted #bbb;margin-bottom:11px}
.service .photo{width:226px;height:89px}
.service p{font-size:9.8px;line-height:13.6px;margin:10px 0 16px;letter-spacing:-.15px}
.partners{left:130px;top:960px;width:720px;height:52px;display:flex;align-items:center;gap:18px}
.partner{background:var(--partner);border-radius:3px}
.footer{left:0;top:1027px;width:965px;height:138px;background:linear-gradient(#d6d6d6,#e2e2e2);border-top:1px solid #c9c9c9}
.footer .brand{left:130px;top:38px;color:#6e6e6e;font-size:12px;line-height:13px;letter-spacing:1.5px}
.footer .brand-dot{background:#6e6e6e;width:38px;height:38px}
.fcol{top:24px}
.fcol h5{font-size:11px;font-weight:700;color:var(--muted);margin-bottom:10px}
.fcol li{list-style:none;font-size:8px;color:#6a6a6a;height:18px;display:flex;align-items:center;gap:6px}
.fcol li::before{content:"";border-left:3px solid #777;border-top:3px solid transparent;border-bottom:3px solid transparent}
.fcol li.on{color:#e0352b}
.contact li::before{display:none}
.contact li{height:22.5px}
.contact svg{width:10px;height:10px;flex:none;margin-right:5px}
.social{display:flex;gap:7px}
.social span{width:27px;height:27px;border-radius:3px;box-shadow:0 1px 2px rgba(0,0,0,.3)}
.bottom{left:0;top:1165px;width:965px;height:35px;background:var(--bar);font-size:8px;color:#aaa}
.bottom .copy{left:126px;top:13px}
.bottom .legal{left:740px;top:13px}
</style>
</head>
<body>

<header class="abs header">
  <div class="abs brand"><span class="brand-dot"></span>VERDANTA ENERGY</div>
  <nav class="abs nav">
    <a class="active" href="#">HOME</a><a href="#">SERVICES</a><a href="#">LATEST NEWS</a><a href="#">ABOUT</a><a href="#">CONTACT</a>
  </nav>
</header>

<section class="abs hero" role="img" aria-label="Smiling technician in a yellow hard hat kneeling beside rooftop solar panels in warm sunlight"></section>
<div class="abs hero-arrow" style="left:0;top:218px"><svg width="47" height="47"><path d="M27 16l-8 7.5 8 7.5" stroke="#fff" stroke-width="2" fill="none"/></svg></div>
<div class="abs hero-arrow" style="left:918px;top:218px"><svg width="47" height="47"><path d="M20 16l8 7.5-8 7.5" stroke="#fff" stroke-width="2" fill="none"/></svg></div>
<div class="abs caption">
  <h2>Verdanta has earned the trust of thousands of Malaysians</h2>
  <p>Choosing to install solar panels in Malaysia due to the quality products and outstanding service we provide.</p>
</div>
<div class="abs hero-edge"></div>

<h2 class="abs heading welcome-title">Welcome to Verdanta Energy</h2>
<div class="abs photo welcome-img" role="img" aria-label="Group portrait of the company team in business attire"></div>
<div class="abs welcome-text">
  <p>Meridian Group of Companies is a diversified corporate enterprise based in India, with operations ranging from manufacture of Surfactants with state of the art process technologies, consultancy in environment and mine designing, surfactants based speciality chemicals and contract manufacturing for home &amp; personal care brands.</p>
  <p>We have 6 plants all over India – Silvassa, Hoogly, Roorkee, Pithampur, Pondicherry, Mangalore.</p>
  <a class="read" href="#">READ MORE</a>
</div>

<h2 class="abs heading news-title">Latest News</h2>
<article class="abs news-item" style="top:508px">
  <div class="photo news-img" role="img" aria-label="Colleagues reviewing a tablet together" style="background:linear-gradient(135deg,#d9dcdf,#4e545b)"></div>
  <div><h4>Irraer sit voluptatem accusantium</h4><p>Proin gravida nibh vel velit auctor aliquet. Aenean sollicitudin, lorem quis bibendum auctor, nisi elit consequat ipsum, nec</p><a href="#">Continue reading...</a></div>
</article>
<article class="abs news-item" style="top:587px">
  <div class="photo news-img" role="img" aria-label="Business handshake over a desk" style="background:linear-gradient(135deg,#e6e8ea,#6e7c8c)"></div>
  <div><h4>Irraer sit voluptatem accusantium</h4><p>Proin gravida nibh vel velit auctor aliquet. Aenean sollicitudin, lorem quis bibendum auctor, nisi elit consequat ipsum, nec</p><a href="#">Continue reading...</a></div>
</article>

<section class="abs service" style="left:128px">
  <h3 class="heading">Energy Management</h3><div class="rule"></div>
  <div class="photo" role="img" aria-label="Electrician in a hard hat in front of a distribution board" style="background:linear-gradient(90deg,#2f4560,#8a97a4 55%,#d6dadd)"></div>
  <p>Lorem ipsum dolor sit amet, consectetur adipisicing elit, sed do eiusmod tempor incididunt ut labore et dolore magna aliqua.</p>
  <a class="read" href="#">READ MORE</a>
</section>
<section class="abs service" style="left:368px">
  <h3 class="heading">LED Lights</h3><div class="rule"></div>
  <div class="photo" role="img" aria-label="Glowing light bulb among bulbs on a bright green surface" style="background:radial-gradient(circle at 50% 40%,#f4ffd0,#b7dc1e 35%,#5c8a0a)"></div>
  <p>Lorem ipsum dolor sit amet, consectetur adipisicing elit, sed do eiusmod tempor incididunt ut labore et dolore magna aliqua.</p>
  <a class="read" href="#">READ MORE</a>
</section>
<section class="abs service" style="left:610px">
  <h3 class="heading">Solar PV Systems</h3><div class="rule"></div>
  <div class="photo" role="img" aria-label="Field of solar panels under a pale sky" style="background:linear-gradient(#cfd9e2 0%,#b7c6d3 25%,#2d3f6b 45%,#23335a 80%,#5d7a3a)"></div>
  <p>Lorem ipsum dolor sit amet, consectetur adipisicing elit, sed do eiusmod tempor incididunt ut labore et dolore magna aliqua.</p>
  <a class="read" href="#">READ MORE</a>
</section>

<div class="abs partners" aria-label="Partner companies">
  <span class="partner" style="width:88px;height:40px"></span>
  <span class="partner" style="width:122px;height:44px"></span>
  <span class="partner" style="width:208px;height:34px"></span>
  <span class="partner" style="width:88px;height:30px"></span>
  <span class="partner" style="width:146px;height:34px"></span>
</div>

<footer class="abs footer">
  <div class="abs brand"><span class="brand-dot"></span><span>VERDANTA<br>ENERGY</span></div>
  <div class="abs fcol" style="left:309px"><h5>Navigation</h5><ul><li>Home</li><li>About</li><li>Services</li><li>Contact</li></ul></div>
  <div class="abs fcol" style="left:430px"><h5>Services</h5><ul><li class="on">Menu1</li><li>Menu1</li><li>Menu1</li><li>Menu1</li></ul></div>
  <div class="abs fcol contact" style="left:550px"><h5>Contact Us</h5><ul>
    <li><svg viewBox="0 0 10 10"><path d="M2 1l2 2-1 1.5c.8 1.5 1.8 2.5 3.3 3.3L7.8 6.8l2 2-1.5 1.2C4.5 9.5.5 5.5 0 1.7z" fill="#777"/></svg>+1800-555-0142</li>
    <li><svg viewBox="0 0 10 10"><rect x="0" y="2" width="10" height="7" fill="#777"/><path d="M0 2l5 4 5-4" stroke="#ddd" fill="none"/></svg>hello@verdanta-energy.com</li>
    <li><svg viewBox="0 0 10 10"><path d="M5 0a3.5 3.5 0 0 1 3.5 3.5C8.5 6 5 10 5 10S1.5 6 1.5 3.5A3.5 3.5 0 0 1 5 0z" fill="#777"/><circle cx="5" cy="3.5" r="1.3" fill="#ddd"/></svg>Your Address, Your Country</li>
    <li style="padding-left:15px">Your Zip Code</li></ul></div>
  <div class="abs fcol" style="left:714px"><h5>Social</h5>
    <div class="social"><span style="background:#3b5998"></span><span style="background:#4aa8e0"></span><span style="background:#1f5e92"></span><span style="background:#d8392b"></span></div>
  </div>
</footer>

<div class="abs bottom">
  <div class="abs copy">Copyright 2014 © CompanyName - All Rights Reserved</div>
  <div class="abs legal">Site Map &nbsp;&nbsp;•&nbsp;&nbsp; Privacy Policy</div>
</div>

</body>
</html>
```